Verdell Chiropractic, achieve your health goals, get better each day one step at a time

A mobile friendly site, fresh look, easy to navigate, has interface with pw/chirply, etc. Blog posts. Uses new logo. Content and address to current site is mirvaton.com. The current site will give you scope of project for content. The logo is not the final but close. Will upload final next week.
Convey the concept that heath is a process, it does not just happen. We take steps to achieve what we want in life including health.

Target Market(s)

30 to 70 year old. Needing health care

Industry/Entity Type

Health Care

Coding

Coded - Design and coding required

Number of Pages Required

5+ page

Font styles to use
Sans Serif

Colors

Designer to choose colors to be used in the design.

Requirements
Must have
• mobile friendly, easy to navigate, PW/Chirply interface, blog, room for current content
Nice to have
• potential for commerce, statistics
Should not have
• Same old look and feel as everything else out there

```html
<!DOCTYPE html>
<html lang="en">
<head>
<meta charset="utf-8">
<title>Verdell Chiropractic</title>
<link href="https://fonts.googleapis.com/css2?family=Roboto:wght@300;400;500;700&display=swap" rel="stylesheet">
<style>
:root{
  --blue:#0b86c9;
  --blue-dark:#0a6ea6;
  --green:#a6cd3f;
  --green-dark:#8cb52b;
  --ink:#222;
  --muted:#555;
  --panel:#f2f2f2;
  --footer:#2e2e2e;
  --white:#fff;
}
*{box-sizing:border-box;margin:0;padding:0}
html,body{width:1200px;height:3629px;overflow:hidden}
body{position:relative;font-family:"Roboto",Arial,sans-serif;color:var(--ink);background:var(--white)}
.abs{position:absolute}
a{color:inherit;text-decoration:none}

/* top bar */
.topbar{left:0;top:0;width:1200px;height:82px}
.topbar .nav{left:0;top:0;width:779px;height:82px;background:var(--blue);display:flex;align-items:center;padding-left:126px}
.topbar .nav a{color:var(--white);font-size:16px;font-weight:500;padding:0 21px;height:82px;line-height:82px}
.topbar .nav a.active{background:var(--blue-dark)}
.topbar .follow{left:779px;top:0;width:421px;height:82px;background:var(--green);display:flex;align-items:center;padding-left:38px;color:var(--white);font-size:16px;font-weight:500}
.topbar .follow .dots{display:flex;gap:10px;margin-left:62px}
.topbar .follow .dots span{width:24px;height:24px;border-radius:50%;background:var(--white)}

/* logo */
.brand{left:0;top:82px;width:1200px;height:140px;display:flex;align-items:center;justify-content:center;gap:12px}
.brand .mark{width:22px;height:22px;border-radius:50%;background:var(--blue)}
.brand .name{font-size:34px;font-weight:700;color:var(--blue);letter-spacing:1px}

/* hero */
.hero{left:0;top:222px;width:1200px;height:576px;
  background:
    radial-gradient(ellipse 260px 200px at 640px 80px,rgba(110,150,190,.85),transparent 70%),
    radial-gradient(ellipse 330px 170px at 240px 330px,rgba(40,40,45,.85),transparent 72%),
    radial-gradient(ellipse 220px 150px at 1070px 460px,rgba(214,184,140,.9),transparent 70%),
    radial-gradient(ellipse 300px 160px at 560px 400px,rgba(236,230,224,.95),transparent 70%),
    radial-gradient(ellipse 180px 120px at 1120px 120px,rgba(200,70,70,.55),transparent 70%),
    linear-gradient(120deg,#c9ccd0 0%,#b7bcc2 45%,#dcdcdc 100%)}
.hero::after{content:"";position:absolute;inset:0;background:rgba(0,0,0,.12)}
.hero .title,.hero .lead,.hero .cta,.hero .arrow{z-index:1}
.hero .title{left:0;top:250px;width:1200px;text-align:center;color:var(--white);font-size:30px;font-weight:300;text-shadow:0 1px 3px rgba(0,0,0,.45)}
.hero .title b{font-weight:700}
.hero .lead{left:0;top:290px;width:1200px;text-align:center;color:var(--white);font-size:14px;line-height:18px;text-shadow:0 1px 2px rgba(0,0,0,.45)}
.hero .cta{left:478px;top:350px;width:244px;height:36px;border-radius:18px;background:var(--green);color:var(--white);font-size:14px;font-weight:500;text-align:center;line-height:36px}
.hero .arrow{top:266px;width:20px;height:36px;background:rgba(255,255,255,.35);color:var(--white);font-size:16px;text-align:center;line-height:36px}
.hero-wave{left:0;top:710px;width:1200px;height:110px}

/* services */
.section-title{left:0;width:1200px;text-align:center;font-size:30px;font-weight:500;color:var(--ink)}
.section-sub{left:0;width:1200px;text-align:center;font-size:14px;line-height:18px;color:var(--muted)}
.service{width:260px;text-align:center;font-size:18px;color:var(--ink);letter-spacing:.5px}
.service svg{display:block;width:76px;height:64px;margin:0 auto 10px}
.services-photo{left:448px;top:968px;width:326px;height:400px;
  background:
    radial-gradient(ellipse 90px 70px at 220px 90px,rgba(120,125,135,.9),transparent 72%),
    radial-gradient(ellipse 110px 150px at 130px 290px,rgba(250,250,250,1),transparent 72%),
    radial-gradient(ellipse 70px 60px at 130px 130px,rgba(200,160,130,.95),transparent 72%),
    radial-gradient(ellipse 80px 60px at 110px 60px,rgba(150,110,80,.85),transparent 72%),
    linear-gradient(180deg,#fff 0%,#f4f4f4 100%)}
.btn-green{height:36px;border-radius:18px;background:var(--green);color:var(--white);font-size:14px;font-weight:500;text-align:center;line-height:36px}

/* conditions */
.conditions{left:0;top:1510px;width:1200px;height:619px;background:var(--blue)}
.condition{width:172px;height:204px;background:var(--white)}
.condition .photo{height:158px;background:var(--g)}
.condition .label{height:46px;background:var(--blue-dark);color:var(--white);font-size:16px;text-align:center;line-height:46px}

/* testimonials + blogs */
.testi-panel{left:121px;top:2298px;width:460px;height:441px;background:var(--panel);padding:14px}
.testi-card{width:432px;height:413px;background:var(--white);text-align:center;padding-top:28px}
.testi-card .avatar{width:104px;height:104px;border-radius:50%;margin:0 auto;border:3px solid #e6e6e6;background:radial-gradient(circle at 50% 38%,#c9a58a 0 24%,transparent 25%),linear-gradient(180deg,#8fa3b8 0 55%,#1f2a38 56%)}
.testi-card .who{margin-top:14px;font-size:17px;font-weight:700;letter-spacing:.5px}
.testi-card .role{font-size:14px;color:var(--green-dark);margin-top:4px}
.testi-card .quote{margin:18px auto 0;width:300px;font-size:14px;line-height:18px;color:var(--muted);position:relative}
.testi-card .quote::before{content:"\201C";position:absolute;left:-28px;top:-10px;font-size:40px;color:var(--ink)}
.testi-card .quote::after{content:"\201D";position:absolute;right:-30px;bottom:-28px;font-size:40px;color:var(--ink)}
.testi-card .more{margin-top:12px;font-size:14px;color:var(--muted)}
.testi-card .pager{display:flex;justify-content:center;gap:6px;margin-top:26px}
.testi-card .pager span{width:7px;height:7px;border-radius:50%;background:#bbb}
.testi-card .pager span.on{background:var(--green)}
.blog-nav{top:2222px;width:30px;height:30px;border-radius:50%;border:2px solid #333;font-size:16px;line-height:26px;text-align:center}
.blog-nav.next{border-color:var(--blue);color:var(--blue)}
.blog-card{left:600px;width:479px;height:213px;background:var(--panel);padding:10px}
.blog-card .photo{left:10px;top:10px;width:222px;height:193px}
.blog-card .date{left:10px;top:10px;width:36px;height:36px;background:var(--green);color:var(--white);font-size:11px;text-align:center;line-height:14px;padding-top:4px}
.blog-card .body{left:248px;top:10px;width:220px}
.blog-card h3{font-size:14px;font-weight:700;letter-spacing:.3px}
.blog-card .meta{display:flex;justify-content:space-between;font-size:12px;color:var(--muted);margin:6px 0 10px}
.blog-card p{font-size:13px;line-height:17px;color:var(--muted);margin-bottom:6px}
.blog-card .more{font-size:13px;color:var(--muted)}

/* contact */
.contact{left:0;top:2811px;width:1200px;height:420px;background:#f6f6f6}
.field{height:38px;border:1px solid #d4d4d4;background:var(--white);font-size:13px;color:#999;padding:11px 10px}
.field.message{height:86px}

/* footer */
.footer-wave{left:0;top:3140px;width:1200px;height:100px}
.footer{left:0;top:3214px;width:1200px;height:354px;background:var(--footer);color:#ddd}
.footer h4{font-size:15px;font-weight:700;color:var(--white);letter-spacing:.5px}
.footer h4::after{content:"";display:block;width:50px;height:2px;background:var(--white);margin-top:8px}
.footer .about{font-size:14px;line-height:19px;color:var(--white)}
.footer ul{list-style:none;font-size:14px;line-height:24px}
.footer ul li::before{content:"\203A";margin-right:14px;color:var(--white)}
.footer .office div{display:flex;gap:18px;font-size:14px;line-height:19px;margin-bottom:6px}
.footer .office i{width:12px;font-style:normal;color:var(--white)}
.footer .subscribe{width:215px;height:34px;background:var(--white);border-radius:3px;display:flex}
.footer .subscribe span{flex:1;font-size:12px;color:#444;line-height:34px;padding-left:10px}
.footer .subscribe b{width:38px;background:var(--green);border-radius:0 3px 3px 0;color:var(--white);font-weight:400;text-align:center;line-height:34px;font-size:14px}
.bottombar{left:0;top:3568px;width:1200px;height:61px;background:var(--blue);color:var(--white);display:flex;align-items:center;padding-left:124px;font-size:15px;font-weight:500}
.bottombar a{margin-right:58px}
.bottombar a.active{text-decoration:underline}
.bottombar .copy{position:absolute;right:122px;font-size:14px}
</style>
</head>
<body>

<header class="abs topbar">
  <nav class="abs nav">
    <a class="active" href="#">Home</a><a href="#">About us</a><a href="#">Services ▾</a><a href="#">Blogs</a><a href="#">Testimonials</a><a href="#">Contact us</a>
  </nav>
  <div class="abs follow">Follow us<div class="dots"><span></span><span></span><span></span><span></span><span></span></div></div>
</header>

<div class="abs brand"><span class="mark"></span><span class="name">VERDELL</span></div>

<section class="abs hero" role="img" aria-label="Chiropractor adjusting a patient's back on a treatment table">
  <div class="abs arrow" style="left:48px">‹</div>
  <div class="abs arrow" style="right:48px">›</div>
  <div class="abs title">Welcome To <b>Verdell Chiropractic</b></div>
  <div class="abs lead">Lorem Ipsum is simply dummy text of the typesetting,<br>printing and typesetting.</div>
  <div class="abs cta">Make an Appointment</div>
</section>
<svg class="abs hero-wave" viewBox="0 0 1200 110" preserveAspectRatio="none">
  <path d="M0 70 C300 10 600 10 1200 22 L1200 110 L0 110Z" fill="#a6cd3f"/>
  <path d="M0 84 C320 32 640 26 1200 40 L1200 110 L0 110Z" fill="#fff"/>
</svg>

<h2 class="abs section-title" style="top:862px">Our Services</h2>
<p class="abs section-sub" style="top:900px">Lorem Ipsum is simply dummy text of the<br>printing and typesetting.</p>

<div class="abs service" style="left:112px;top:962px">
  <svg viewBox="0 0 76 64" role="img" aria-label="Treatment table icon"><rect x="8" y="34" width="60" height="8" rx="3" fill="#0b86c9"/><rect x="14" y="42" width="5" height="16" fill="#0b86c9"/><rect x="57" y="42" width="5" height="16" fill="#0b86c9"/><rect x="24" y="24" width="30" height="8" rx="4" fill="#0b86c9"/></svg>Chiropractic</div>
<div class="abs service" style="left:112px;top:1124px">
  <svg viewBox="0 0 76 64" role="img" aria-label="Herbal bowl icon"><path d="M38 8 C54 12 56 28 40 34 C30 28 28 16 38 8Z" fill="#0b86c9"/><path d="M14 34 H62 C62 50 50 58 38 58 C26 58 14 50 14 34Z" fill="#0b86c9"/></svg>Homeopathy</div>
<div class="abs service" style="left:112px;top:1290px">
  <svg viewBox="0 0 76 64" role="img" aria-label="Needle icon"><rect x="8" y="46" width="60" height="8" rx="3" fill="#0b86c9"/><line x1="24" y1="44" x2="50" y2="10" stroke="#0b86c9" stroke-width="3"/><line x1="36" y1="44" x2="60" y2="16" stroke="#0b86c9" stroke-width="3"/><circle cx="50" cy="10" r="4" fill="#0b86c9"/><circle cx="60" cy="16" r="4" fill="#0b86c9"/></svg>Acupunture</div>
<div class="abs service" style="left:812px;top:962px">
  <svg viewBox="0 0 76 64" role="img" aria-label="Muscle test icon"><rect x="10" y="44" width="56" height="8" rx="3" fill="#0b86c9"/><rect x="16" y="52" width="5" height="8" fill="#0b86c9"/><rect x="55" y="52" width="5" height="8" fill="#0b86c9"/><rect x="34" y="8" width="8" height="34" rx="4" fill="#0b86c9"/><path d="M44 16 L58 10" stroke="#0b86c9" stroke-width="4" stroke-linecap="round"/></svg>Applied Kinesiology</div>
<div class="abs service" style="left:812px;top:1124px">
  <svg viewBox="0 0 76 64" role="img" aria-label="Spine icon"><rect x="30" y="2" width="16" height="8" rx="3" fill="#0b86c9"/><rect x="28" y="13" width="18" height="9" rx="3" fill="#0b86c9"/><rect x="27" y="25" width="20" height="9" rx="3" fill="#0b86c9"/><rect x="28" y="37" width="20" height="9" rx="3" fill="#0b86c9"/><rect x="30" y="49" width="18" height="10" rx="3" fill="#0b86c9"/></svg>Spinal Therapy</div>
<div class="abs service" style="left:812px;top:1290px">
  <svg viewBox="0 0 76 64" role="img" aria-label="Massage table icon"><rect x="6" y="36" width="64" height="8" rx="3" fill="#0b86c9"/><rect x="12" y="44" width="5" height="16" fill="#0b86c9"/><rect x="59" y="44" width="5" height="16" fill="#0b86c9"/><circle cx="16" cy="28" r="6" fill="#0b86c9"/><rect x="26" y="24" width="38" height="10" rx="5" fill="#0b86c9"/></svg>Massge</div>
<div class="abs services-photo" role="img" aria-label="Therapist treating a seated woman's shoulders"></div>
<div class="abs btn-green" style="left:506px;top:1410px;width:190px">View More</div>

<section class="abs conditions">
  <div class="abs condition" style="left:121px;top:94px;--g:radial-gradient(ellipse 60px 70px at 90px 70px,#e2b89c,transparent 75%),linear-gradient(160deg,#8a5a3c,#d9d2cc)"><div class="photo" role="img" aria-label="Woman with a headache"></div><div class="label">Headaches</div></div>
  <div class="abs condition" style="left:317px;top:94px;--g:radial-gradient(ellipse 70px 50px at 110px 110px,#f2f2f2,transparent 75%),linear-gradient(150deg,#e8e8e8,#c79a7f 55%,#eeeeee)"><div class="photo" role="img" aria-label="Neck pain treatment"></div><div class="label">Neck Pain</div></div>
  <div class="abs condition" style="left:515px;top:94px;--g:radial-gradient(ellipse 50px 60px at 60px 70px,#8d8f94,transparent 75%),linear-gradient(160deg,#f0f0f0,#d9ad92 60%,#f4f4f4)"><div class="photo" role="img" aria-label="Shoulder pain treatment"></div><div class="label">Shoulder Pain</div></div>
  <div class="abs condition" style="left:711px;top:94px;--g:radial-gradient(ellipse 70px 50px at 90px 90px,#d6a487,transparent 75%),linear-gradient(160deg,#f5f5f5,#e9e4e0)"><div class="photo" role="img" aria-label="Hands holding a painful wrist"></div><div class="label">Wrist Pain</div></div>
  <div class="abs condition" style="left:907px;top:94px;--g:radial-gradient(ellipse 30px 30px at 70px 60px,#d2453b,transparent 75%),linear-gradient(150deg,#5c5f66,#c9a691 55%,#7b7f86)"><div class="photo" role="img" aria-label="Highlighted shoulder muscle pain"></div><div class="label">Fibromyalgia</div></div>
  <div class="abs condition" style="left:121px;top:318px;--g:radial-gradient(ellipse 60px 80px at 90px 70px,#b57a58,transparent 75%),linear-gradient(170deg,#e9e2dc,#9c6648)"><div class="photo" role="img" aria-label="Lower back pain"></div><div class="label">Lower Back</div></div>
  <div class="abs condition" style="left:317px;top:318px;--g:radial-gradient(ellipse 60px 70px at 100px 80px,#e0b49a,transparent 75%),linear-gradient(160deg,#f1f1f1,#4b4b52)"><div class="photo" role="img" aria-label="Hip and leg pain"></div><div class="label">Pain Hip &amp; Leg Pain</div></div>
  <div class="abs condition" style="left:515px;top:318px;--g:radial-gradient(ellipse 40px 50px at 80px 50px,#d8a98c,transparent 75%),linear-gradient(180deg,#b99a86,#2f3a4f 55%,#1f2838)"><div class="photo" role="img" aria-label="Knee pain"></div><div class="label">Knee Pain</div></div>
  <div class="abs condition" style="left:711px;top:318px;--g:radial-gradient(ellipse 80px 40px at 90px 100px,#d89d80,transparent 75%),linear-gradient(160deg,#efe7e2,#c88a6e)"><div class="photo" role="img" aria-label="Heel pain massage"></div><div class="label">Heel Pain</div></div>
  <div class="abs condition" style="left:907px;top:318px;--g:radial-gradient(ellipse 30px 30px at 60px 80px,#f0b43a,transparent 75%),radial-gradient(ellipse 60px 70px at 90px 80px,#e8dcc4,transparent 75%),linear-gradient(160deg,#ffffff,#d8d2c6)"><div class="photo" role="img" aria-label="Spinal disc model"></div><div class="label">Disc Bulge</div></div>
</section>

<h2 class="abs" style="left:121px;top:2218px;width:460px;text-align:center;font-size:30px;font-weight:500">Testimonials</h2>
<p class="abs" style="left:121px;top:2258px;width:460px;text-align:center;font-size:14px;color:#555">Lorem Ipsum is simply dummy text.</p>
<div class="abs testi-panel">
  <div class="testi-card">
    <div class="avatar" role="img" aria-label="Client portrait"></div>
    <div class="who">CALVIN MORROW</div>
    <div class="role">Creative Director</div>
    <div class="quote">Lorem Ipsum is simply dummy text of the printing and typesetting .Lorem Ipsum industry.</div>
    <div class="more">Read More..◎</div>
    <div class="pager"><span class="on"></span><span></span><span></span></div>
    <div class="btn-green" style="width:190px;margin:18px auto 0">View More</div>
  </div>
</div>

<h2 class="abs" style="left:782px;top:2220px;font-size:30px;font-weight:500">Blogs</h2>
<div class="abs blog-nav" style="left:1012px">‹</div>
<div class="abs blog-nav next" style="left:1050px">›</div>

<article class="abs blog-card" style="top:2298px">
  <div class="abs photo" role="img" aria-label="Hands massaging a lower back" style="background:radial-gradient(ellipse 70px 60px at 120px 80px,#e2b8a0,transparent 75%),radial-gradient(ellipse 120px 40px at 110px 180px,#9fb6d6,transparent 75%),linear-gradient(150deg,#6e3f2d,#c4917a 55%,#8a5745)"></div>
  <div class="abs date">01<br>Sep</div>
  <div class="abs body">
    <h3>BLOG POST TITLE</h3>
    <div class="meta"><span>▦ 05Feb , 2018</span><span>◯ 20</span></div>
    <p>Lorem Ipsum is simply dummy text of the And printing matter and typesetting industry.</p>
    <p>Ipsum is simply dummy text of the And printing matter and type setting industry.</p>
    <div class="more">Read More..◎</div>
  </div>
</article>
<article class="abs blog-card" style="top:2528px">
  <div class="abs photo" role="img" aria-label="Hands treating a patient's knee" style="background:radial-gradient(ellipse 50px 50px at 170px 160px,#c0262c,transparent 75%),radial-gradient(ellipse 80px 70px at 100px 80px,#e8b9a0,transparent 75%),linear-gradient(150deg,#5a2e22,#b98067 55%,#7a3f30)"></div>
  <div class="abs date">01<br>Sep</div>
  <div class="abs body">
    <h3>BLOG POST TITLE</h3>
    <div class="meta"><span>▦ 05Feb , 2018</span><span>◯ 20</span></div>
    <p>Lorem Ipsum is simply dummy text of the And printing matter and typesetting industry.</p>
    <p>Ipsum is simply dummy text of the And printing matter and type setting industry.</p>
    <div class="more">Read More..◎</div>
  </div>
</article>

<section class="abs contact">
  <h2 class="abs section-title" style="top:50px;font-size:28px">Quick Contact Form</h2>
  <div class="abs field" style="left:126px;top:120px;width:230px">Full Name</div>
  <div class="abs field" style="left:364px;top:120px;width:230px">Last Name</div>
  <div class="abs field" style="left:603px;top:120px;width:230px">Email</div>
  <div class="abs field" style="left:843px;top:120px;width:231px">Phone</div>
  <div class="abs field message" style="left:126px;top:170px;width:948px">Message</div>
  <div class="abs btn-green" style="left:506px;top:287px;width:190px">Submit</div>
</section>
<svg class="abs footer-wave" viewBox="0 0 1200 100" preserveAspectRatio="none">
  <path d="M0 60 C400 100 800 20 1200 10 L1200 100 L0 100Z" fill="#a6cd3f"/>
  <path d="M0 78 C400 110 800 40 1200 34 L1200 100 L0 100Z" fill="#2e2e2e"/>
</svg>

<footer class="abs footer">
  <div class="abs" style="left:121px;top:60px;display:flex;align-items:center;gap:10px">
    <span style="width:18px;height:18px;border-radius:50%;background:var(--blue)"></span>
    <span style="font-size:30px;font-weight:700;color:var(--blue);letter-spacing:1px">VERDELL</span>
  </div>
  <p class="abs about" style="left:121px;top:160px;width:210px">Lorem Ipsum is simply dummy text of the printing and typese tting industry. Lorem Ipsum has been the industry's standard.</p>
  <div class="abs" style="left:121px;top:248px;font-size:14px;font-weight:700;color:#fff">Read More ⓘ</div>

  <div class="abs" style="left:411px;top:64px">
    <h4>QUICK LINKS</h4>
    <ul style="margin-top:22px"><li>Home</li><li>About us</li><li>Services</li><li>Blogs</li><li>Testimonials</li><li>Contact us</li></ul>
  </div>

  <div class="abs office" style="left:590px;top:64px;width:240px">
    <h4 style="margin-left:37px">OFFICE</h4>
    <div style="margin-top:22px"><i>⌖</i><span>Dorian Vaske DC PA<br>4870 Larkspur Road West<br>Brenton, TX 70415</span></div>
    <div><i>✆</i><span>555.204.7731</span></div>
    <div><i>✉</i><span>info@mirvaton.com</span></div>
    <div><i>◷</i><span>Mon-Sat 9:00am-6 :00pm</span></div>
  </div>

  <div class="abs" style="left:861px;top:64px;width:230px">
    <h4>SUBSCRIBE</h4>
    <p style="margin-top:22px;font-size:14px;line-height:22px;color:#fff">Get the latest updates and offer Lorem Ipsum is simply dummy text of the printing.</p>
    <div class="subscribe" style="margin-top:26px"><span>Enter Your Email</span><b>✉</b></div>
  </div>
</footer>

<nav class="abs bottombar">
  <a class="active" href="#">HOME</a><a href="#">ABOUT US</a><a href="#">SERVICES</a><a href="#">BLOG</a><a href="#">CONTACT</a>
  <span class="copy">© 2018 VERDELL - ALL RIGHTS RESERVED</span>
</nav>

</body>
</html>
```